New Bicycle shop business card

Hi!
I'm looking for a business card for my new proffesional bike mechanics shop. This shop is only for fixing broken bikes and not selling bikes.
Peferbly a modern and sleek and modern design.
Colors: black, grey, red, white
Information:
Name: Velowerkplaats Martens
Shop owner: Bart Martens & Sofie Vanhulle
Website: www.velowerkplaats-martens.be
Email: info@velowerkplaats-martens.be
Phone number: +32471936208
Street adres: Molenweg 57
9470 Hoevedonk
Slogan/shop information: Herstellingen van alle merken.
Logo: see files.
Target Market(s)
People who seek a mechanic to fix or upgrade their bikes.
Contact Information for Business Card
Information:
Website: info@velowerkplaats-martens.be
9470 Hoevedonk
Logo: see files.

```html
<!DOCTYPE html>
<html lang="nl">
<head>
<meta charset="utf-8">
<title>Velowerkplaats Martens – visitekaartje</title>
<link href="https://fonts.googleapis.com/css2?family=Montserrat:wght@800&family=Open+Sans:wght@400;600&display=swap" rel="stylesheet">
<style>
  :root {
    --bg: #3a3a3a;
    --black: #161616;
    --white: #ffffff;
    --paper: #f7f7f7;
    --red: #dc1f3e;
    --grey: #8a8a8a;
    --ink: #222222;
  }
  * { margin: 0; padding: 0; box-sizing: border-box; }
  html, body { width: 1200px; height: 1021px; overflow: hidden; }
  body { background: var(--bg); position: relative; font-family: "Open Sans", sans-serif; }

  .card { position: absolute; width: 700px; height: 400px; overflow: hidden; box-shadow: 0 12px 30px rgba(0,0,0,.45); }
  .card svg.bands { position: absolute; inset: 0; }

  /* back */
  .card--back { left: 380px; top: 70px; background: var(--black); color: var(--white); text-align: center; }
  .wordmark { display: flex; align-items: center; justify-content: center; gap: 14px; font-family: "Montserrat", sans-serif; font-weight: 800; letter-spacing: 2px; }
  .wordmark__dot { width: 18px; height: 18px; background: var(--red); }
  .card--back .wordmark { margin-top: 130px; font-size: 34px; color: var(--white); }
  .tagline { margin-top: 22px; display: flex; align-items: center; justify-content: center; gap: 10px; font-size: 18px; }
  .tagline::before, .tagline::after { content: ""; width: 26px; height: 2px; background: var(--red); }
  .card--back .site { margin-top: 26px; font-size: 18px; letter-spacing: 2px; }
  .site__name { color: var(--red); }

  /* front */
  .card--front { left: 160px; top: 500px; background: var(--paper); color: var(--ink); }
  .card--front .wordmark { position: absolute; left: 50px; top: 60px; font-size: 28px; color: var(--ink); justify-content: flex-start; }
  .divider { position: absolute; left: 50px; right: 130px; top: 170px; height: 1px; background: var(--grey); }
  .address { position: absolute; left: 50px; top: 215px; font-size: 19px; line-height: 1.3; font-style: normal; }
  .owners { position: absolute; right: 40px; top: 190px; text-align: right; }
  .owners__names { color: var(--red); font-weight: 600; font-size: 22px; }
  .owners__role { font-size: 19px; }
  .contact { position: absolute; right: 40px; top: 262px; text-align: right; font-size: 18px; line-height: 1.45; list-style: none; }
  .contact li { display: flex; align-items: center; justify-content: flex-end; gap: 8px; }
  .contact svg { width: 16px; height: 16px; }
  .card--front .site { position: absolute; right: 40px; bottom: 10px; color: var(--white); font-size: 20px; }
</style>
</head>
<body>

<section class="card card--back" aria-label="Achterkant">
  <svg class="bands" viewBox="0 0 700 400" aria-hidden="true">
    <polygon points="170,372 530,372 522,400 178,400" fill="var(--red)"/>
  </svg>
  <div class="wordmark"><span class="wordmark__dot"></span>VELOWERKPLAATS MARTENS</div>
  <p class="tagline">Herstellingen van alle merken.</p>
  <p class="site">www.<span class="site__name">velowerkplaats-martens</span>.be</p>
</section>

<section class="card card--front" aria-label="Voorkant">
  <svg class="bands" viewBox="0 0 700 400" aria-hidden="true">
    <polygon points="0,318 440,360 440,366 0,330" fill="var(--black)"/>
    <polygon points="0,336 450,372 480,354 700,354 700,400 0,400" fill="var(--red)"/>
  </svg>
  <div class="wordmark"><span class="wordmark__dot"></span>VELOWERKPLAATS MARTENS</div>
  <div class="divider"></div>
  <address class="address">Molenweg 57<br>9470 Hoevedonk</address>
  <div class="owners">
    <p class="owners__names">Bart Martens &amp; Sofie Vanhulle</p>
    <p class="owners__role">Shop Owner</p>
  </div>
  <ul class="contact">
    <li>+32471936208
      <svg viewBox="0 0 24 24" aria-label="telefoon"><path fill="var(--red)" d="M6.6 10.8a15 15 0 0 0 6.6 6.6l2.2-2.2c.3-.3.7-.4 1-.2 1.1.4 2.3.6 3.6.6.6 0 1 .4 1 1V20c0 .6-.4 1-1 1A17 17 0 0 1 3 4c0-.6.4-1 1-1h3.5c.6 0 1 .4 1 1 0 1.3.2 2.5.6 3.6.1.3 0 .7-.2 1z"/></svg>
    </li>
    <li>info@velowerkplaats-martens.be
      <svg viewBox="0 0 24 24" aria-label="e-mail"><rect x="2" y="5" width="20" height="14" fill="none" stroke="var(--red)" stroke-width="2"/><path d="M2 5l10 8 10-8" fill="none" stroke="var(--red)" stroke-width="2"/></svg>
    </li>
  </ul>
  <p class="site">www.velowerkplaats-martens.be</p>
</section>

</body>
</html>
```